Strong, Clean Book Design Needed for "The Lantern Keeper"

I need a strong, clean, masculine cover of a book that focuses on helping men restore honor to what it means to be a good husband. (I also need a back cover and spine done as well). I would like the cover to be either a white, red, or black cover. I have attached 3 books that I would like to use as examples to model after. I also attached a word document to show the potential layouts I would like to see and how that parallel the example covers.

Specs:
- Book is 150 pages long
- Size is 5.25 x 8

Target Market(s)

Christian men who are married or looking to be married.

Font styles to use
Serif
Sans Serif

Colors
ec1f27
f04a50
ffffff
000000
1b1b1b
757575

Requirements
Must have
• - A design that resembles/has a similar feel to one of the three examples that are attached and laid out similarly to one of the 3 designs in the word doc "3 Book Designs"
• - These elements on the front cover: Title: The Lantern Keeper, Subtitle: Renewing the Courage of a Faith-Led Marriage, Author Name: Dale Forsby
• - A strong design that is simple yet creative.
• - Strong masculine font that is bold but not too flashy
• - Red should be included either as the title font color or as the overall cover color.
• - The back of the book should have the attached file "Back of the book" text on the back
Nice to have
• - A color contrast, like a strip of another color (see "example 3" attached file) across the front for the subtitle or the author name.
• - Including the attached sword file as a somewhat transparent image on the cover, but absolutely not necessary.
• - If there is going to be any highlighting of words in the subtitle, they should be the word "honor" and "Christ-centered"
Should not have
• Any religious symbols, such as a cross.

```html
<!DOCTYPE html>
<html lang="en">
<head>
<meta charset="utf-8">
<title>The Lantern Keeper — Book Cover Wrap</title>
<link href="https://fonts.googleapis.com/css2?family=Alfa+Slab+One&family=Poppins:wght@300;400&display=swap" rel="stylesheet">
<style>
  :root {
    --cover-red: #bf262d;
    --cover-red-deep: #9e1c22;
    --ink: #1b1b1b;
    --black: #000000;
    --white: #ffffff;
    --stage: #e8e4dd;
  }
  * { margin: 0; padding: 0; box-sizing: border-box; }
  html, body { width: 1200px; height: 800px; overflow: hidden; }
  body { background: var(--stage); position: relative; font-family: "Poppins", sans-serif; }

  .wrap { position: absolute; left: 165px; top: 80px; width: 870px; height: 640px; display: flex; box-shadow: 0 12px 30px rgba(0,0,0,.25); }

  .cover { position: relative; width: 420px; height: 640px;
    background: radial-gradient(ellipse at 50% 40%, var(--cover-red) 0%, var(--cover-red-deep) 100%); overflow: hidden; }

  /* Back cover */
  .back__title { position: absolute; right: 28px; top: 22px; text-align: right; font-family: "Alfa Slab One", serif; line-height: 1; }
  .back__the { font-size: 15px; color: var(--black); }
  .back__main { font-size: 34px; color: var(--white); }
  .back__sub { font-size: 24px; color: var(--black); }
  .back__copy { position: absolute; left: 40px; right: 32px; top: 140px; color: var(--white); font-size: 9.6px; line-height: 1.38; text-align: justify; }
  .back__copy p { margin-bottom: 11px; }
  .back__lead { text-align: right; }
  .back__tag { font-family: "Alfa Slab One", serif; color: var(--black); font-size: 11px; line-height: 1.4; margin-top: 4px; text-align: left; }
  .back__author { position: absolute; left: 40px; right: 32px; bottom: 78px; display: flex; align-items: center; gap: 14px; }
  .author-photo { width: 84px; height: 84px; border-radius: 50%; background: var(--black); flex: none; }
  .back__bio { color: var(--white); font-size: 9px; line-height: 1.45; }

  /* Spine */
  .spine { width: 30px; height: 640px; background: var(--ink); display: flex; flex-direction: column; justify-content: space-between; align-items: center; padding: 16px 0; }
  .spine__text { writing-mode: vertical-rl; font-family: "Alfa Slab One", serif; color: var(--white); font-size: 13px; letter-spacing: .5px; }

  /* Front cover */
  .front__the { position: absolute; top: 50px; width: 100%; text-align: center; font-family: "Alfa Slab One", serif; font-size: 30px; line-height: 1.2; color: var(--black); }
  .front__main { position: absolute; top: 118px; width: 100%; text-align: center; font-family: "Alfa Slab One", serif; font-size: 62px; line-height: 1.2; color: var(--white); letter-spacing: -1px; }
  .sword-art { position: absolute; left: 14px; top: 196px; width: 392px; height: 20px; border-radius: 10px;
    background: linear-gradient(90deg, #2a2a2a 0%, #5a5a5a 30%, #d7d7d7 60%, #b0b0b0 100%); opacity: .9; }
  .front__sub-title { position: absolute; top: 234px; width: 100%; text-align: center; font-family: "Alfa Slab One", serif; font-size: 48px; line-height: 1.2; color: var(--black); }
  .steel-strip { position: absolute; left: 0; top: 350px; width: 420px; height: 128px; }
  .front__subtitle { position: absolute; left: 0; top: 380px; width: 100%; text-align: center; font-weight: 300; font-size: 20px; line-height: 1.4; color: var(--ink); letter-spacing: .3px; }
  .front__author { position: absolute; top: 548px; width: 100%; text-align: center; font-family: "Alfa Slab One", serif; font-size: 36px; line-height: 1.2; color: var(--white); letter-spacing: 1px; }
</style>
</head>
<body>
<div class="wrap">
  <section class="cover back">
    <div class="back__title">
      <div class="back__the">THE</div>
      <div class="back__main">LANTERN</div>
      <div class="back__sub">KEEPER</div>
    </div>
    <div class="back__copy">
      <p class="back__lead">Will you be the one who keeps the flame burning?</p>
      <p>Long before electric light, every harbor town trusted a keeper to tend its lantern through the night. He rose in the dark, trimmed the wick, cleaned the glass and stood his watch through storm and calm alike. Ships came home because one faithful man refused to let the light go out, and whole villages were shaped by his quiet steadiness.</p>
      <p>The Lantern Keeper is a practical guide for men who want to lead their homes with that same faithfulness. Drawing on the call to love sacrificially, Dale walks husbands through the daily habits of tending a marriage: listening well, serving first, guarding trust and carrying light into hard seasons. Each chapter closes with simple steps a husband can take this week, not someday.</p>
      <p>This is an invitation to every husband to pick up the lantern again, to stand his post, and to keep the light burning for the people he loves most.</p>
      <p class="back__tag">Take up the watch of a faithful husband.<br>Keep the light for your home.</p>
    </div>
    <div class="back__author">
      <div class="author-photo" role="img" aria-label="Author portrait photo"></div>
      <p class="back__bio">DALE FORSBY is the pastor of Harborview Church, where he loves helping men grow in faith. He has been married to his wife, Anna, for over a decade, and together they raise their beautiful daughters.</p>
    </div>
  </section>

  <section class="spine">
    <span class="spine__text">THE LANTERN KEEPER</span>
    <span class="spine__text">DALE FORSBY</span>
  </section>

  <section class="cover front">
    <div class="front__the">THE</div>
    <div class="front__main">LANTERN</div>
    <div class="sword-art" role="img" aria-label="Sword illustration with red ribbon"></div>
    <div class="front__sub-title">KEEPER</div>
    <svg class="steel-strip" viewBox="0 0 420 128" aria-hidden="true">
      <defs>
        <linearGradient id="steelGrad" x1="0" x2="1" y1="0" y2="0">
          <stop offset="0" stop-color="#8f8f8f"/>
          <stop offset=".5" stop-color="#cfcfcf"/>
          <stop offset="1" stop-color="#a4a4a4"/>
        </linearGradient>
      </defs>
      <polygon fill="url(#steelGrad)" points="0,14 40,10 80,16 120,8 150,6 175,0 200,10 250,6 300,4 340,8 380,2 420,4 420,96 390,100 350,96 300,104 250,102 200,108 180,114 150,110 110,118 70,122 30,124 0,128"/>
    </svg>
    <div class="front__subtitle">RENEWING THE COURAGE OF A<br>FAITH-LED MARRIAGE</div>
    <div class="front__author">DALE FORSBY</div>
  </section>
</div>
</body>
</html>
```